I need a website for my moving company Bolt Hauling LLC. I would like the following text included in my website. I have purchased the domain bolthaulingcrew.example from siteburrow.example. I am not familiar with SEO or other techniques that help my page on search engines but would like the website to be optimized for Findora search engine. I have attached our logo below and would like it to be used in the design. The colors in the logo can be used also in the design.
Home/About Us
At Bolt Hauling LLC, we know moving. It can be difficult, stressful, and a real pain in the backside. But it doesn’t have to be! When you partner with Bolt, you get the benefits of a professional moving team that is licensed and insured for your protection along with years of experience and a dedication to providing the highest quality service, each and every time.
Our Services
We do a wide variety of local moves, including apartments, single-family homes, retirement communities, dorms, condos, and many more! Our movers are trained to protect your belongings and your home – all pieces of furniture are padded and stretch wrapped free of charge, ensuring your items and home are damage-free at the end of your move. Having added stress about packing up your home prior to moving? We’ve got you covered with our full service packing and unpacking services, too.
What You Get
When you partner with BOLT, you’ll get the best service in the industry, as well as:
* The Use of Packing & Moving Materials: The hourly rate includes the use of our dollies, ratchet straps, pads, moving tools, and property protection like floor mats, door-jamb protectors, stairwell protectors, and plenty of muscle!
• Trained, Licensed, and Insured Movers: All of our movers are highly trained to provide you with the best service, and to ensure the protection of you and your items.
• Professional: Honest, Uniformed, Nice, Knowledgeable Service is what you’ll get with every member of our moving teams.
• Custom Service for Every Move: Every move is as unique as the person or business moving. Our training and equipment allows us to customize every project to ensure the very best for every client.
Target Market(s)
Home and Business movers
Industry/Entity Type
Moving Company
Colors
Designer to choose colors to be used in the design.
Requirements
Must have
- 2 sides
Nice to have
- Colorful design with logo included.
Should not have
- animated characters

```html
<!DOCTYPE html>
<html lang="en">
<head>
<meta charset="utf-8">
<title>Bolt Hauling LLC</title>
<link href="https://fonts.googleapis.com/css2?family=Raleway:wght@500;600;700&family=Open+Sans:wght@400;600;700&display=swap" rel="stylesheet">
<style>
:root{
  --green:#8cc63f;
  --orange:#f7941d;
  --ink:#333333;
  --text:#555555;
  --dark:#1e1e1e;
  --light:#f2f2f2;
  --white:#ffffff;
}
*{margin:0;padding:0;box-sizing:border-box}
html,body{width:1200px;height:3180px;overflow:hidden}
body{position:relative;font-family:"Open Sans",Arial,sans-serif;color:var(--text);background:var(--white)}
.abs{position:absolute}
.btn{position:absolute;display:flex;align-items:center;justify-content:center;border-radius:22px;color:var(--white);font:700 13px "Raleway",sans-serif;text-transform:uppercase;letter-spacing:.3px}
.btn-green{background:var(--green)}
.btn-orange{background:var(--orange)}
.btn-dark{background:#3a3a3a}
.heading{font-family:"Raleway",sans-serif;font-weight:600;color:var(--ink)}

/* header */
.site-header{left:0;top:0;width:1200px;height:95px;background:var(--dark)}
.brand{display:flex;align-items:center;gap:10px}
.brand-mark{width:26px;height:26px;background:var(--orange)}
.brand-name{font:700 22px "Raleway",sans-serif;color:var(--orange);text-transform:uppercase}
.site-header .brand{position:absolute;left:60px;top:33px}
.nav{position:absolute;top:0;height:95px;display:flex;align-items:center;color:var(--white);font:700 13px "Raleway",sans-serif;text-transform:uppercase}
.nav-how{left:563px}.nav-pricing{left:729px}.nav-contact{left:829px}
.nav-book{left:928px;top:27px;width:135px;height:42px}

/* hero */
.hero{left:0;top:95px;width:1200px;height:535px;background:linear-gradient(100deg,#3b3734 0%,#5a4d44 40%,#6b5647 70%,#453a33 100%)}
.hero-title{left:60px;top:262px;font:600 86px "Raleway",sans-serif;color:var(--white)}
.hero-sub{left:60px;top:362px;font:600 28px "Raleway",sans-serif;color:var(--white)}
.hero-book{left:60px;top:428px;width:135px;height:42px}
.hero-call{left:225px;top:440px;font:700 12px "Raleway",sans-serif;color:var(--green);text-transform:uppercase}
.hero-phone{left:328px;top:430px;font:600 27px "Open Sans",sans-serif;color:var(--white)}

/* about */
.about-kicker{left:60px;top:702px;font:500 15px "Raleway",sans-serif;color:var(--orange)}
.about-title{left:57px;top:732px;font-size:34px}
.about-text{left:60px;top:790px;width:545px;font-size:13.5px;line-height:22px}
.about-more{left:55px;top:943px;width:135px;height:42px}

/* quote */
.quote{left:678px;top:558px;width:467px;height:481px;background:var(--white);box-shadow:0 4px 14px rgba(0,0,0,.18)}
.quote-head{height:72px;background:var(--green);display:flex;align-items:center;justify-content:center;color:var(--white);font:700 21px "Raleway",sans-serif;text-transform:uppercase}
.field{position:absolute;left:19px;width:427px;height:47px;background:var(--white);border:1px solid #ececec;display:flex;align-items:center;gap:12px;padding-left:16px;font-size:13px;color:#777}
.field svg{width:16px;height:16px}
.field-desc{height:112px;align-items:flex-start;padding-top:16px}
.quote-send{left:168px;top:410px;width:152px;height:43px}

/* guarantee */
.guarantee{left:0;top:1075px;width:1200px;height:505px;background:var(--light)}
.guarantee-photo{left:64px;top:63px;width:540px;height:399px;background:linear-gradient(120deg,#d9d2c6,#efe9df 50%,#c9b49a);box-shadow:0 3px 10px rgba(0,0,0,.15)}
.guarantee-kicker{left:662px;top:112px;font:500 15px "Raleway",sans-serif;color:var(--green)}
.guarantee-title{left:660px;top:142px;font-size:34px}
.guarantee-text{left:667px;top:202px;width:380px;font-size:13.5px;line-height:22px}
.guarantee-list{left:670px;top:276px;list-style:none;font-size:14.5px;color:#444}
.guarantee-list li{position:relative;padding-left:20px;height:33px}
.guarantee-list li::before{content:"";position:absolute;left:0;top:6px;width:6px;height:6px;background:var(--green)}

/* pricing */
.pricing{left:0;top:1580px;width:1200px;height:530px;border-top:6px solid var(--green);background:linear-gradient(90deg,#c7b39c 0%,#b99c7c 35%,#9b7a5d 65%,#7e5f45 100%)}
.price-card{left:64px;top:42px;width:439px;height:435px;background:rgba(255,255,255,.88);text-align:center}
.price-name{position:absolute;left:0;right:0;top:66px;font-size:34px}
.price-unit{position:absolute;left:0;right:0;top:124px;font-size:19px;color:#555}
.price-amount{position:absolute;left:0;right:0;top:168px;font:700 46px "Open Sans",sans-serif;color:#444}
.price-book{left:150px;top:286px;width:134px;height:43px}

/* services */
.services{left:0;top:2110px;width:1200px;height:508px;background:linear-gradient(180deg,#f6f6f6,#e9e9e9)}
.services-title{left:0;width:1200px;top:96px;text-align:center;font:700 34px "Raleway",sans-serif;color:var(--orange)}
.services-text{left:168px;top:170px;width:864px;text-align:center;font-size:15px;line-height:23px;color:#444}
.services-more{left:528px;top:345px;width:151px;height:41px}

/* contact */
.contact .brand{position:absolute;left:68px;top:2660px}
.contact-title{left:62px;top:2742px;font:500 22px "Raleway",sans-serif;color:#222}
.contact-text{left:62px;top:2784px;width:390px;font-size:15px;line-height:23px;color:#666}
.contact-company{left:62px;top:2848px;font-size:15px;color:#333}
.contact-address{left:62px;top:2892px;font-size:15px;color:#333}
.contact-phone{left:62px;top:2928px;font-size:24px;color:#333}
.contact-message{left:57px;top:2990px;width:153px;height:42px}
.map{left:483px;top:2663px;width:691px;height:360px;background:linear-gradient(135deg,#e4e4e0,#d9dbd5)}

/* footer */
.site-footer{left:0;top:3075px;width:1200px;height:105px;background:var(--dark)}
.copyright{position:absolute;left:62px;top:45px;font-size:12px;color:#9a9a9a}
.social{position:absolute;top:37px;width:30px;height:30px;border-radius:50%}
</style>
</head>
<body>

<header class="abs site-header">
  <div class="brand"><span class="brand-mark"></span><span class="brand-name">Bolt Hauling</span></div>
  <span class="nav nav-how">How it works</span>
  <span class="nav nav-pricing">Pricing</span>
  <span class="nav nav-contact">Contact</span>
  <span class="btn btn-green nav-book">Book now</span>
</header>

<section class="abs hero" role="img" aria-label="Movers in uniform unloading boxes from a moving truck while a couple watches"></section>
<h1 class="abs hero-title">Fast Moving ?</h1>
<p class="abs hero-sub">See How We Do It</p>
<span class="btn btn-orange hero-book">Book now</span>
<span class="abs hero-call">Or call now</span>
<span class="abs hero-phone">(601) 555-0148</span>

<p class="abs about-kicker">we are bolthauling</p>
<h2 class="abs heading about-title">Experienced &amp; Reliable</h2>
<p class="abs about-text">At Bolt Hauling LLC, we know moving. It can be difficult, stressful, and a real pain in the backside. But it doesn’t have to be! When you partner with Bolt, you get the benefits of a professional moving team that is licensed and insured for your protection along with years of experience and a dedication to providing the highest quality service, each and every time.</p>
<span class="btn btn-green about-more">Read more</span>

<section class="abs guarantee">
  <div class="abs guarantee-photo" role="img" aria-label="Two people packing household items into a cardboard box"></div>
  <p class="abs guarantee-kicker">Fully insured</p>
  <h2 class="abs heading guarantee-title">Our Gaurantee</h2>
  <p class="abs guarantee-text">When you partner with BOLT, you’ll get the best service in the industry, as well as:</p>
  <ul class="abs guarantee-list">
    <li>The unlimited use of packing &amp; moving materials</li>
    <li>Trained, Licensed, and Insured Movers</li>
    <li>A Professional service catering to your specific needs</li>
  </ul>
</section>

<form class="abs quote">
  <div class="quote-head">Get a quote</div>
  <div class="field" style="top:98px"><svg viewBox="0 0 16 16" fill="none" stroke="#555" stroke-width="1.3"><circle cx="8" cy="5" r="3"/><path d="M2.5 15c0-3.2 2.5-5 5.5-5s5.5 1.8 5.5 5"/></svg>Name</div>
  <div class="field" style="top:160px"><svg viewBox="0 0 16 16" fill="none" stroke="#555" stroke-width="1.3"><rect x="1.5" y="3.5" width="13" height="9"/><path d="M1.5 3.5 8 9l6.5-5.5"/></svg>Email</div>
  <div class="field" style="top:224px"><svg viewBox="0 0 16 16" fill="none" stroke="#555" stroke-width="1.3"><path d="M3 1.5h3l1 3.5-2 1.3a8 8 0 0 0 4.7 4.7L11 9l3.5 1v3a1.5 1.5 0 0 1-1.5 1.5A11.5 11.5 0 0 1 1.5 3 1.5 1.5 0 0 1 3 1.5z"/></svg>Phone</div>
  <div class="field field-desc" style="top:289px"><svg viewBox="0 0 16 16" fill="none" stroke="#555" stroke-width="1.3"><path d="M2 14l1-4 8-8 3 3-8 8z"/><path d="M9.5 3.5l3 3"/></svg>Description</div>
  <span class="btn btn-orange quote-send">Send request</span>
</form>

<section class="abs pricing" role="img" aria-label="Couple sitting on a wooden floor with mugs beside moving boxes">
  <div class="abs price-card">
    <h3 class="heading price-name">Moving Service</h3>
    <p class="price-unit">1 hour</p>
    <p class="price-amount">$125.00</p>
    <span class="btn btn-green price-book">Book now</span>
  </div>
</section>

<section class="abs services">
  <h2 class="abs services-title">Our Services</h2>
  <p class="abs services-text">Bolt Hauling LLC in Brookfield does a wide variety of local moves, including apartments, single-family homes, retirement communities, dorms, condos, and many more! Our movers are trained to protect your belongings and your home – all pieces of furniture are padded and stretch wrapped free of charge, ensuring your items and home are damage-free at the end of your move. Having added stress about packing up your home prior to moving? We’ve got you covered with our full service packing and unpacking services, too.</p>
  <span class="btn btn-dark services-more">Read more</span>
</section>

<section class="contact">
  <div class="brand"><span class="brand-mark"></span><span class="brand-name">Bolt Hauling</span></div>
  <h2 class="abs contact-title">Schedule Your Move</h2>
  <p class="abs contact-text">To arrange movers, please contact us at your convenience. We look forward to meeting you soon.</p>
  <p class="abs contact-company">Bolt Hauling LLC</p>
  <p class="abs contact-address">742 Alder Ln., Brookfield, MS 39000, US</p>
  <p class="abs contact-phone">(601) 555-0148</p>
  <span class="btn btn-green contact-message">Message now</span>
  <div class="abs map" role="img" aria-label="Street map showing the company location"></div>
</section>

<footer class="abs site-footer">
  <p class="copyright">Copyright © 2017 Bolt Hauling LLC - All Rights Reserved.</p>
  <span class="social" style="left:1017px;background:#3b5998"></span>
  <span class="social" style="left:1060px;background:#1da1f2"></span>
  <span class="social" style="left:1102px;background:#0077b5"></span>
  <span class="social" style="left:1145px;background:#6dbf4b"></span>
</footer>

</body>
</html>
```